Permanent Makeup (cosmetics salon) Brochure

We need a 2-4 sites brochure for our Permanent Makeup (cosmetics salon). Our company is based in Austria / Vienna. -> Our homepage is www.mk-lorenzhuber.at
This brochure should show which treatments we provide ot our customers.

I've uploaded our old brochure, the content (text) would be nearly the same (look form "Must Haves", pics have to be new (look uploaded pics)
The old brochure is to dark. -> look for our homepage maybe you can make it like this

Target Market(s)

woman, age 25-70 years who wants to have permanent makeup on eyebrows, lips or eyeliner

Industry/Entity Type

Beauty Salon

Requirements
Must have
• pics which are uploaded.

*This text (somithing about our business)
"Für Frau Lorenzhuber ist Permanent Makeup ein Kunsthandwerk. Das Team von MK-Lorenzhuber ist spezialisiert auf natürliches Permanent Makeup damit der individuelle Typ jeder Kundin am schönsten zum Ausdruck kommt."

*We do this treatments: (english)
+ Augenbrauen Microblading (eyebrows)
+ Augenbrauen Permanent Makeup (eyebrows2)
+ Lidstrich Permanent Makeup (eyeliner)
+ Lip Blushing (lips)
+ Lippen Permanent Makeup (lips2)

* Our addresses (2 locations)
Wien
Kerngasse 7b/12, 1010 Wien
Tel: 01/5827316

Villach
Birkenhofweg 24, 9524 St. Ulrich
Tel: 0676/3158940

Mail: info@mk-lorenzhuber.at
www.mk-lorenzhuber.at

```html
<!DOCTYPE html>
<html lang="de">
<head>
<meta charset="utf-8">
<title>Marika Lorenzhuber – Broschüre</title>
<link rel="stylesheet" href="https://fonts.googleapis.com/css2?family=Josefin+Sans:wght@300;400&display=swap">
<style>
  :root {
    --stage: #c6c6c6;
    --paper: #ffffff;
    --ink: #231f20;
    --text: #2b2b2b;
    --gold: #d5b24a;
    --on-dark: #f2f2f2;
  }
  * { box-sizing: border-box; margin: 0; padding: 0; }
  html, body { width: 1200px; height: 2426px; overflow: hidden; }
  body {
    background: var(--stage);
    font-family: "Josefin Sans", "Helvetica Neue", Arial, sans-serif;
    font-weight: 300;
    color: var(--text);
    position: relative;
  }
  .spread {
    position: absolute;
    left: 40px;
    width: 1120px;
    height: 556px;
    background: var(--paper);
    box-shadow: 0 6px 24px rgba(0,0,0,.18);
    overflow: hidden;
  }
  .spread--covers { top: 617px; }
  .spread--inside { top: 1253px; }
  .block { position: absolute; }
  .dark { background: var(--ink); color: var(--on-dark); }
  .photo { position: absolute; }

  /* studio name */
  .studio-name {
    font-size: 20px;
    font-weight: 300;
    color: var(--on-dark);
    letter-spacing: .5px;
    white-space: nowrap;
  }

  /* back cover */
  .tagline { left: 0; top: 0; width: 560px; height: 135px; display: flex; align-items: center; justify-content: center; text-align: center; font-size: 12.5px; line-height: 1.45; color: var(--text); padding-top: 8px; }
  .contact { left: 0; top: 349px; width: 560px; height: 207px; }
  .contact .studio-name { position: absolute; left: 66px; top: 56px; }
  .address { position: absolute; top: 134px; font-size: 10px; line-height: 1.5; color: var(--on-dark); }
  .address__city { color: var(--gold); }
  .address--wien { left: 66px; }
  .address--villach { left: 222px; }
  .address--online { left: 405px; top: 149px; color: var(--gold); }

  /* front cover */
  .cover-head { left: 560px; top: 0; width: 560px; height: 135px; }
  .cover-head .studio-name { position: absolute; right: 70px; top: 58px; }
  .headline { position: absolute; left: 620px; top: 372px; color: var(--text); }
  .headline__main { font-size: 60px; line-height: 1; }
  .headline__sub { font-size: 19px; margin-top: 6px; }
  .headline__end { font-size: 52px; line-height: 1; margin-top: 2px; }
  .web-tag { position: absolute; left: 944px; top: 503px; height: 16px; display: flex; }
  .web-tag__label { background: var(--gold); color: var(--ink); font-size: 10px; padding: 3px 10px 0; width: 162px; text-align: center; white-space: nowrap; }
  .web-tag__end { background: var(--ink); width: 14px; }

  /* inside left */
  .eyecatch { left: 51px; top: 141px; width: 162px; height: 102px; padding: 26px 0 0; text-align: center; }
  .eyecatch__small { font-size: 10px; }
  .eyecatch__accent { font-size: 10px; color: var(--gold); margin: 1px 0; }
  .eyecatch__big { font-size: 19px; letter-spacing: .3px; }
  .about { left: 51px; top: 272px; width: 440px; font-size: 11px; line-height: 1.45; color: var(--text); }
  .footer-band { left: 0; top: 351px; width: 560px; height: 205px; }
  .footer-band .studio-name { position: absolute; left: 0; right: 0; top: 72px; text-align: center; }
  .footer-band__contact { position: absolute; left: 0; right: 0; top: 148px; text-align: center; font-size: 10.5px; color: var(--on-dark); }
  .footer-band__sep { color: var(--gold); margin: 0 6px; }

  /* inside right */
  .treatments { position: absolute; left: 782px; top: 72px; color: var(--text); }
  .treatments__intro { font-size: 19px; }
  .treatments__title { font-size: 54px; line-height: 1; margin-top: 6px; letter-spacing: .5px; }
  .treatment-list { position: absolute; left: 658px; top: 207px; list-style: none; font-size: 12px; color: var(--text); }
  .treatment-list li { display: flex; align-items: center; gap: 8px; height: 25px; }
  .treatment-list li::before { content: ""; width: 10px; height: 10px; border: 1px solid var(--gold); border-radius: 50%; }
</style>
</head>
<body>

<section class="spread spread--covers" aria-label="Umschlag">
  <p class="block tagline">Ihr Kosmetikstudio und Beauty Salon in 1010 Wien Professionelles Microblading<br>und Permanent Make Up für gehobene Ansprüche</p>
  <div class="photo" role="img" aria-label="Nahaufnahme eines geschminkten Auges mit langen Wimpern" style="left:0;top:135px;width:560px;height:214px;background:linear-gradient(90deg,#a37a60 0%,#c79a7c 35%,#8a6048 65%,#1a1616 100%);"></div>
  <div class="block dark contact">
    <div class="studio-name">Marika Lorenzhuber</div>
    <p class="address address--wien"><span class="address__city">Wien</span><br>Kerngasse 7b/12, 1010 Wien<br>Tel: 01/5827316</p>
    <p class="address address--villach"><span class="address__city">Villach</span><br>Birkenhofweg 24, 9524 St. Ulrich<br>Tel: 0676/3158940</p>
    <p class="address address--online">info@mk-lorenzhuber.at<br>www.mk-lorenzhuber.at</p>
  </div>

  <div class="block dark cover-head">
    <div class="studio-name">Marika Lorenzhuber</div>
  </div>
  <div class="photo" role="img" aria-label="Frau mit hellem Haar, Blick in die Kamera" style="left:560px;top:135px;width:560px;height:214px;background:linear-gradient(90deg,#e8dccb 0%,#d7a98c 35%,#c98a6c 60%,#e3c9ae 100%);"></div>
  <div class="headline">
    <div class="headline__main">Schönheit</div>
    <div class="headline__sub">kommt nicht nur von</div>
    <div class="headline__end">innen</div>
  </div>
  <div class="web-tag"><span class="web-tag__label">www.mk-lorenzhuber.at</span><span class="web-tag__end"></span></div>
</section>

<section class="spread spread--inside" aria-label="Innenseiten">
  <div class="photo" role="img" aria-label="Augenpartie mit definierten Augenbrauen" style="left:0;top:0;width:440px;height:171px;background:linear-gradient(90deg,#b58a6e 0%,#d6b29a 45%,#c69a80 80%,#2a2020 100%);"></div>
  <div class="photo" role="img" aria-label="Auge mit Lidstrich in Nahaufnahme" style="left:440px;top:0;width:262px;height:171px;background:linear-gradient(90deg,#d9b8a0 0%,#c99c80 50%,#6e4a3a 100%);"></div>
  <div class="block dark eyecatch">
    <div class="eyecatch__small">Macht jeden Augenblick zu</div>
    <div class="eyecatch__accent">einer</div>
    <div class="eyecatch__big">AUGENWEIDE</div>
  </div>
  <p class="block about">Für Frau Lorenzhuber ist Permanent Makeup ein Kunsthandwerk. Das Team von MK-Lorenzhuber ist spezialisiert auf natürliches Permanent Makeup damit der individuelle Typ jeder Kundin am schönsten zum Ausdruck kommt.</p>
  <div class="block dark footer-band">
    <div class="studio-name">Marika Lorenzhuber</div>
    <p class="footer-band__contact">info@mk-lorenzhuber.at<span class="footer-band__sep">|</span>www.mk-lorenzhuber.at</p>
  </div>

  <div class="treatments">
    <div class="treatments__intro">We do this</div>
    <div class="treatments__title">Treatments</div>
  </div>
  <ul class="treatment-list">
    <li>Augenbrauen Microblading (eyebrows)</li>
    <li>Augenbrauen Permanent Makeup (eyebrows2)</li>
    <li>Lidstrich Permanent Makeup (eyeliner)</li>
    <li>Lip Blushing (lips)</li>
    <li>Lippen Permanent Makeup (lips2)</li>
  </ul>
  <div class="photo" role="img" aria-label="Lippen mit Lip Blushing in Nahaufnahme" style="left:560px;top:351px;width:289px;height:205px;background:linear-gradient(180deg,#e9cbbb 0%,#d99a8a 50%,#ecd3c5 100%);"></div>
  <div class="photo" role="img" aria-label="Volle Lippen mit Permanent Makeup" style="left:858px;top:351px;width:262px;height:205px;background:linear-gradient(180deg,#dcb09c 0%,#d38678 50%,#e5c0ae 100%);"></div>
</section>

</body>
</html>
```